TALVORIK

The business want a professional looking business card. We have a scetch we will add but want the extra upgrade, and would like more suggestions for variations of our business cards.

```html
<!DOCTYPE html>
<html lang="en">
<head>
<meta charset="UTF-8">
<title>TALVORIK Business Card</title>
<link rel="stylesheet" href="https://fonts.googleapis.com/css2?family=Montserrat:wght@400;500;600;700&display=swap">
<style>
  :root {
    --bg: #1c1c1c;
    --card: #1f1f20;
    --card-edge: #2a2a2b;
    --gold: #c9962e;
    --gold-light: #e2b750;
    --text-light: #ededed;
    --gloss: #2e2e30;
    --gloss-light: #3a3a3d;
  }
  * { margin: 0; padding: 0; box-sizing: border-box; }
  html, body { width: 1200px; height: 801px; overflow: hidden; }
  body {
    background: var(--bg);
    font-family: "Montserrat", sans-serif;
    display: flex;
    align-items: center;
    justify-content: center;
    gap: 48px;
  }
  .card {
    width: 530px;
    height: 303px;
    border-radius: 18px;
    background: var(--card);
    border: 1px solid var(--card-edge);
    box-shadow: 0 18px 40px rgba(0,0,0,0.55);
    position: relative;
    overflow: hidden;
  }

  /* Front */
  .card-front .identity {
    position: absolute;
    left: 40px;
    top: 42px;
  }
  .wordmark {
    color: var(--gold);
    font-weight: 600;
    font-size: 34px;
    letter-spacing: 6px;
    line-height: 1;
  }
  .tagline {
    color: var(--gold);
    font-size: 9px;
    letter-spacing: 6px;
    margin-top: 8px;
    margin-left: 60px;
  }
  .person { margin-top: 26px; }
  .person-name {
    color: var(--gold-light);
    font-weight: 700;
    font-size: 20px;
  }
  .person-role {
    color: var(--text-light);
    font-size: 14px;
    margin-top: 2px;
  }
  .accent-square {
    position: absolute;
    left: 0;
    top: 176px;
    width: 26px;
    height: 26px;
    background: var(--gold);
  }
  .contacts {
    list-style: none;
    position: absolute;
    left: 40px;
    bottom: 34px;
  }
  .contacts li {
    display: flex;
    align-items: center;
    gap: 10px;
    color: var(--text-light);
    font-size: 13.5px;
    line-height: 24px;
  }
  .contacts svg { width: 12px; height: 12px; fill: var(--gold); flex: none; }

  .front-mark {
    position: absolute;
    right: 46px;
    top: 52px;
    display: flex;
    flex-direction: column;
    align-items: center;
    gap: 12px;
  }
  .mark-circle {
    width: 96px;
    height: 96px;
    border-radius: 50%;
    background: var(--gloss);
  }
  .mark-name {
    color: var(--gloss-light);
    font-weight: 600;
    font-size: 16px;
    letter-spacing: 4px;
  }

  /* Back */
  .card-back {
    display: flex;
    flex-direction: column;
    align-items: center;
    justify-content: center;
    gap: 14px;
    background: linear-gradient(135deg, #232324 0%, #1b1b1c 60%, #202021 100%);
  }
  .back-circle {
    width: 86px;
    height: 86px;
    border-radius: 50%;
    background: var(--gloss);
  }
  .back-wordmark {
    color: var(--gloss-light);
    font-weight: 600;
    font-size: 30px;
    letter-spacing: 6px;
  }
  .back-tagline {
    color: var(--gloss-light);
    font-size: 9px;
    letter-spacing: 6px;
    margin-top: -8px;
  }
</style>
</head>
<body>
  <section class="card card-front">
    <div class="identity">
      <div class="wordmark">TALVORIK</div>
      <div class="tagline">SINCE 2026</div>
      <div class="person">
        <div class="person-name">Aksel Rune Marstad</div>
        <div class="person-role">CEO &amp; Founder</div>
      </div>
    </div>
    <span class="accent-square"></span>
    <ul class="contacts">
      <li>
        <svg viewBox="0 0 24 24"><path d="M6.6 10.8a15 15 0 0 0 6.6 6.6l2.2-2.2a1 1 0 0 1 1-.25 11.4 11.4 0 0 0 3.6.6 1 1 0 0 1 1 1V20a1 1 0 0 1-1 1A17 17 0 0 1 3 4a1 1 0 0 1 1-1h3.5a1 1 0 0 1 1 1c0 1.25.2 2.45.6 3.6a1 1 0 0 1-.25 1z"/></svg>
        004790012345
      </li>
      <li>
        <svg viewBox="0 0 24 24"><path d="M2 5h20v14H2zm2 2v.5l8 5 8-5V7z"/></svg>
        talvorik.llc@postmail.com
      </li>
      <li>
        <svg viewBox="0 0 24 24"><circle cx="12" cy="12" r="10"/></svg>
        www.talvorik.llc
      </li>
    </ul>
    <div class="front-mark">
      <span class="mark-circle"></span>
      <span class="mark-name">TALVORIK</span>
    </div>
  </section>

  <section class="card card-back">
    <span class="back-circle"></span>
    <div class="back-wordmark">TALVORIK</div>
    <div class="back-tagline">SINCE 2026</div>
  </section>
</body>
</html>
```